I want your CD Cover design for my next singe "After Marlow Fell"

I'm looking for a CD cover based on my song "After Marlow Fell". It's a reflection on the passing of my musical influences (Gareth Lindqvist, Ned Thorn, Rupert Vanley) and other (e.g. Talon), and on those still with us (e.g. Pemberton) and what we do when those who influenced us most are gone from our lives.

You should be able to listen to a private demo unreleased version here:

https://www.tunecellar.net/quietmeadowguild/song/58214067-after-marlow-fell-demo-mix-rn

I prefer influenced/metaphoric images vs. direct copies (e.g. no pictures of famous musicians), but I'll leave that to your creativity for the details.

Looking forward to seeing everyone's designs!

Otto Selvik
c/o Quiet Meadow Guild
www.quietmeadowguild.net

Target Market(s)

Indie-pop, classic rock

Requirements
Must have
• Quiet Meadow Guild logo in the image (eps and psd files provided)
• After Marlow Fell logo in the image
Should not have
• Should not have direct pictures of musicians noted above on the artwork
• Should not have my name (Otto Selvik) on the artwork
• Should not have the website on the artwork

```html
<!DOCTYPE html>
<html lang="en">
<head>
<meta charset="utf-8">
<title>After Marlow Fell — Quiet Meadow Guild</title>
<link rel="stylesheet" href="https://fonts.googleapis.com/css2?family=Oswald:wght@300;400&display=swap">
<style>
  :root {
    --backdrop-top: #e4e4e4;
    --backdrop-bottom: #c9c9c9;
    --sky-light: #eef1f2;
    --sky-cloud: #c9d6dc;
    --horizon: #9fb3bd;
    --sea-mid: #3f5a6b;
    --sea-deep: #2a3d4d;
    --shore-dark: #242c45;
    --ink: #14181c;
    --title-band: rgba(16, 22, 30, 0.82);
    --title-ink: #f4f6f8;
  }
  * { margin: 0; padding: 0; box-sizing: border-box; }
  html, body {
    width: 1200px;
    height: 802px;
    overflow: hidden;
  }
  body {
    background: linear-gradient(180deg, var(--backdrop-top), var(--backdrop-bottom));
    display: flex;
    align-items: center;
    justify-content: center;
    font-family: "Oswald", sans-serif;
  }
  .cover {
    position: relative;
    width: 720px;
    height: 720px;
    overflow: hidden;
    box-shadow: 0 10px 30px rgba(0, 0, 0, 0.25);
  }
  .cover-photo {
    position: absolute;
    inset: 0;
    background:
      radial-gradient(ellipse 45% 22% at 88% 80%, rgba(20, 26, 48, 0.75), transparent 70%),
      linear-gradient(180deg,
        var(--sky-light) 0%,
        var(--sky-cloud) 22%,
        var(--sky-light) 34%,
        var(--horizon) 38.5%,
        var(--sea-mid) 40%,
        var(--sea-deep) 62%,
        var(--shore-dark) 100%);
  }
  .band-name {
    position: absolute;
    top: 62px;
    left: 255px;
    color: var(--ink);
    font-weight: 300;
    text-transform: uppercase;
    line-height: 0.98;
    letter-spacing: 0.06em;
  }
  .band-name span { display: block; font-size: 62px; }
  .band-name .line-2 { padding-left: 44px; }
  .band-name .line-3 { padding-left: 96px; font-size: 52px; }
  .single-title {
    position: absolute;
    right: 34px;
    bottom: 96px;
    padding: 6px 18px 8px;
    background: var(--title-band);
    color: var(--title-ink);
    font-weight: 300;
    font-size: 46px;
    letter-spacing: 0.12em;
    text-transform: uppercase;
    line-height: 1.1;
  }
</style>
</head>
<body>
  <main class="cover">
    <div class="cover-photo" role="img" aria-label="Photograph of a calm grey-blue lake under a pale cloudy sky, with waves breaking over dark pebbles and rocks in the foreground"></div>
    <h1 class="band-name">
      <span class="line-1">Quiet</span>
      <span class="line-2">Meadow</span>
      <span class="line-3">Guild</span>
    </h1>
    <h2 class="single-title">After Marlow Fell</h2>
  </main>
</body>
</html>
```